Business Value Optimisation Consultancy Needs a Web Design

Velor Quintess is a business consultancy in Australia, which assists SMEs (small; to medium sized businesses) to grow revenue signicantly, put in professional operaations, and become worth a lot more as a sale-able business.

It is in need of new website design (you can see the current "old" site here at www.velorquintess.net - please note all content has changed for the new site - please see content file attached).

An example of a site we like is www.bluekestrelhub.com.au because:

a. it is crisp and clear, and quickly conveys what the offering is all about.
b. it offers a report download with email sign up.
c. it is easy and simple to navigate

We don't want an exact copy of this site, but this site is given as an example of the type of clear design we like.

Another example is:

Also, please see the attached powerpoint presentation - please note the style used in it - we would like the website to be close to the powerpoint style but it does not have to be exactly the same.

2. please see attached files with:

a. content for all pages - note the content makes reference to some videos
b. a list of all available videos, as hosted on vimeo
c. blog posts written to date
d. a powerpoint presentation used by Velor Quintess - please keep the site design in line with the style used in this powerpoint presentation.

Designs to be supplied as PSD files.

Thank you!

Target Market(s)

Small to Medium Sized Professional Service Businesses
Technology Start Ups
Medium Businesses Approaching Small Corporate Size

Industry/Entity Type

Business Consultant

Number of Pages Required

3 page

Font styles to use
Sans Serif

Requirements
Must have
• Home Page
• Inner Page
• Blog

```html
<!DOCTYPE html>
<html lang="en">
<head>
<meta charset="utf-8">
<title>Velor Quintess – Business Value Optimisation</title>
<link href="https://fonts.googleapis.com/css2?family=Open+Sans:ital,wght@0,400;0,600;0,700;0,800;1,400;1,600;1,700&display=swap" rel="stylesheet">
<style>
:root{
  --navy:#1f3a5c;
  --blue:#1d9ad6;
  --blue-dark:#1583bb;
  --light-blue:#6fc6ee;
  --pale-blue:#d3ebf8;
  --purple:#a23a8f;
  --purple-dark:#8a2f7a;
  --grey-bg:#f1f1f1;
  --text:#3c3c3c;
  --muted:#6b6b6b;
  --white:#ffffff;
}
*{box-sizing:border-box;margin:0;padding:0}
html,body{width:1200px;height:2820px;overflow:hidden}
body{font-family:"Open Sans",Arial,sans-serif;color:var(--text);background:var(--white);position:relative}
.main-nav,.brand,.tagline,.hero,.recognise,.growth,.learn,.guide,.site-footer,.bottom-bar{position:absolute;left:0;width:1200px}

/* navigation */
.main-nav{top:0;height:32px;background:var(--navy);display:flex;justify-content:center}
.main-nav a{color:var(--white);font-size:12px;font-weight:600;text-decoration:none;padding:0 22px;line-height:32px;letter-spacing:.4px}
.main-nav a.active{background:var(--blue)}

/* brand */
.brand{top:32px;height:120px;display:flex;flex-direction:column;align-items:center;justify-content:center}
.brand-row{display:flex;align-items:center;gap:14px}
.brand-mark{width:30px;height:30px;background:var(--blue)}
.brand-name{font-size:34px;font-weight:700;color:var(--navy);letter-spacing:.5px}
.brand-sub{font-size:13px;color:var(--muted);margin-top:4px}

.tagline{top:152px;height:48px;text-align:center;font-style:italic;font-weight:700;font-size:23px;color:var(--blue-dark);line-height:48px}

/* hero */
.hero{top:200px;height:580px;background:var(--blue)}
.hero-title{position:absolute;top:48px;width:100%;text-align:center;color:var(--white);font-size:44px;font-weight:700;line-height:1.2}
.hero-pitch{position:absolute;left:110px;top:268px;color:var(--white);font-size:30px;font-weight:400;line-height:1.35}
.hero-pitch strong{color:var(--navy);font-weight:700}
.btn-outline{position:absolute;left:110px;top:420px;width:118px;height:50px;border:2px solid var(--white);color:var(--white);font-weight:700;font-size:16px;display:flex;align-items:center;justify-content:center}
.hero-dash{position:absolute;left:240px;top:340px}
.video-frame{position:absolute;left:628px;top:220px;width:470px;height:270px;background:var(--white);padding:8px;box-shadow:0 6px 16px rgba(0,0,0,.2)}
.video-fill{width:100%;height:100%;background:linear-gradient(#f7f7f7,#e6e6e6);display:flex;align-items:center;justify-content:center}

/* recognise */
.recognise{top:780px;height:380px}
.head-illustration{position:absolute;left:150px;top:70px;width:260px;height:240px;background:linear-gradient(160deg,#b44ea0,var(--purple-dark));border-radius:6px}
.recognise-body{position:absolute;left:560px;top:72px;width:540px}
.recognise-body h2{font-size:25px;font-weight:700;color:var(--navy);line-height:1.3}
.recognise-body h3{font-size:16px;font-style:italic;font-weight:700;color:var(--navy);margin:16px 0 14px}
.tick-list{list-style:none}
.tick-list li{display:flex;gap:12px;font-size:13px;line-height:1.4;margin-bottom:14px;color:var(--muted)}
.tick-list svg{flex:none;margin-top:2px}

/* growth */
.growth{top:1160px;height:340px;background:var(--purple)}
.growth-body{position:absolute;left:190px;top:50px;width:420px;color:var(--white)}
.growth-body h2{font-size:24px;font-weight:700;line-height:1.3;margin-bottom:22px}
.arrow-list{list-style:none}
.arrow-list li{display:flex;justify-content:space-between;gap:18px;font-size:13px;line-height:1.4;margin-bottom:14px;padding-left:80px}
.arrow-list .mark{flex:none;font-weight:700}
.growth-illustration{position:absolute;left:730px;top:50px;width:300px;height:240px;background:var(--purple-dark);border-radius:6px}

/* learn */
.learn{top:1500px;height:480px;text-align:center}
.learn h2{margin-top:42px;font-size:24px;font-weight:700;color:var(--navy)}
.learn h3{margin-top:6px;font-size:16px;font-style:italic;font-weight:600;color:var(--navy)}
.learn h3 em{color:var(--blue-dark);font-weight:700}
.video-row{display:flex;justify-content:center;gap:16px;margin-top:26px}
.video-thumb{width:280px;height:200px;background:linear-gradient(135deg,#c9ced4,#8d959e)}
.learn p{width:620px;margin:30px auto 0;font-size:13px;line-height:1.5;color:var(--muted)}
.learn p strong{color:var(--blue-dark)}

/* guide */
.guide{top:1980px;height:440px;background:var(--blue)}
.consult-arrow{position:absolute;left:420px;top:40px}
.guide-box{position:absolute;left:110px;top:64px;width:260px;height:246px;background:var(--navy);color:var(--white);padding:34px 28px;font-size:19px;line-height:1.45}
.guide-box strong{color:var(--light-blue);font-weight:600}
.btn-download{position:absolute;left:110px;top:310px;width:260px;height:84px;background:var(--purple);color:var(--white);font-weight:800;font-size:19px;line-height:1.25;display:flex;align-items:center;justify-content:center;text-align:center;padding:0 20px}
.consult-text{position:absolute;left:660px;top:110px;width:380px;text-align:right;color:var(--navy);font-size:17px;line-height:1.5}
.consult-text strong{font-weight:700}
.consult-text em{color:var(--blue-dark)}
.consult-link{position:absolute;left:660px;top:290px;width:380px;text-align:right;font-size:15px;font-style:italic;font-weight:600;color:var(--blue-dark);text-decoration:underline}

/* footer */
.site-footer{top:2420px;height:340px;background:var(--grey-bg)}
.foot-col{position:absolute;top:50px}
.foot-col h4{font-size:17px;font-weight:700;color:var(--navy);margin-bottom:16px}
.foot-col p{font-size:12px;line-height:1.5;color:var(--muted)}
.contact{left:100px;width:270px}
.contact .phone{color:var(--blue-dark);font-weight:700;font-size:14px;margin-top:14px}
.contact .mail{color:var(--blue-dark);font-size:12px;margin-top:6px;text-decoration:underline}
.newsletter{left:486px;width:300px}
.newsletter h5{font-size:16px;font-weight:700;color:var(--navy);margin:22px 0 12px}
.signup{display:flex}
.signup .field{width:220px;height:30px;background:var(--white);border:1px solid #d3d3d3;font-size:11px;color:#999;padding:0 10px;line-height:28px}
.signup .go{width:34px;height:30px;background:var(--blue);color:var(--white);font-size:11px;font-weight:700;text-align:center;line-height:30px}
.sitemap{left:866px;width:240px}
.sitemap-links{display:flex;justify-content:space-between}
.sitemap-links ul{list-style:none}
.sitemap-links li{font-size:12px;color:var(--muted);margin-bottom:8px}

.bottom-bar{top:2760px;height:60px;background:var(--navy);color:var(--white);font-size:11px}
.bottom-bar .copyright{position:absolute;left:100px;top:22px}
.socials{position:absolute;left:900px;top:18px;display:flex;gap:8px}
.socials span{width:24px;height:24px;border-radius:50%;border:1.5px solid var(--white)}
</style>
</head>
<body>

<nav class="main-nav">
  <a class="active">HOME</a><a>WHO WE ARE</a><a>WHAT WE DO</a><a>WHO WE WORK WITH</a><a>RESOURCES</a><a>EVENTS</a><a>BLOG</a><a>CONTACT US</a>
</nav>

<header class="brand">
  <div class="brand-row"><span class="brand-mark"></span><span class="brand-name">Velor Quintess</span></div>
  <div class="brand-sub">The Business Value Optimisers</div>
</header>

<div class="tagline">Forward-thinking strategies to grow your business and optimise its potential!</div>

<section class="hero">
  <h1 class="hero-title">You want your business to flourish.<br>But you're afraid of the potential risk</h1>
  <p class="hero-pitch">You CAN grow your business<br>with a game-changing <strong>strategy</strong>.<br>Safely.</p>
  <div class="btn-outline">SEE HOW</div>
  <svg class="hero-dash" width="380" height="110" viewBox="0 0 380 110">
    <path d="M0 100 C120 100 220 60 360 40" fill="none" stroke="#fff" stroke-width="2.5" stroke-dasharray="8 7"/>
    <path d="M350 30 L372 38 L356 54" fill="none" stroke="#fff" stroke-width="2.5"/>
  </svg>
  <div class="video-frame">
    <div class="video-fill" role="img" aria-label="Intro video still: the consultancy shows how to optimise your business value">
      <svg width="70" height="50" viewBox="0 0 70 50"><rect width="70" height="50" rx="10" fill="#c9302c"/><path d="M28 15 L47 25 L28 35Z" fill="#fff"/></svg>
    </div>
  </div>
</section>

<section class="recognise">
  <div class="head-illustration" role="img" aria-label="Illustration of a head in profile containing a lightbulb and gears"></div>
  <div class="recognise-body">
    <h2>We help entrepreneurial businesses reach their true potential and maximise their market value.</h2>
    <h3>Do you recognize your business?</h3>
    <ul class="tick-list">
      <li><svg width="12" height="12" viewBox="0 0 12 12"><path d="M1 6 L5 10 L11 2" fill="none" stroke="#1d9ad6" stroke-width="2"/></svg>You have big plans for growth, but aren't sure how to implement them</li>
      <li><svg width="12" height="12" viewBox="0 0 12 12"><path d="M1 6 L5 10 L11 2" fill="none" stroke="#1d9ad6" stroke-width="2"/></svg>You fear the risk and additional capital commitment it would take to grow</li>
      <li><svg width="12" height="12" viewBox="0 0 12 12"><path d="M1 6 L5 10 L11 2" fill="none" stroke="#1d9ad6" stroke-width="2"/></svg>You own a successful SME but it has yet to reach its full potential</li>
      <li><svg width="12" height="12" viewBox="0 0 12 12"><path d="M1 6 L5 10 L11 2" fill="none" stroke="#1d9ad6" stroke-width="2"/></svg>If you sold your business today, you aren't sure you would get what it's worth</li>
    </ul>
  </div>
</section>

<section class="growth">
  <div class="growth-body">
    <h2>Your business grows from good to great when together we:</h2>
    <ul class="arrow-list">
      <li>Identify the issues holding you back<span class="mark">&#8250;</span></li>
      <li>Develop a three year strategic plan<span class="mark">&#8250;</span></li>
      <li>Position your company for rapid success with the right management, distribution and financial models<span class="mark">&#8250;</span></li>
      <li>Optimise your company's financial value in the marketplace<span class="mark">&#8250;</span></li>
    </ul>
  </div>
  <div class="growth-illustration" role="img" aria-label="Illustration of a clock, a team of people and a rising chart"></div>
</section>

<section class="learn">
  <h2>Want to learn more?</h2>
  <h3><em>What we bring:</em> Perspective – Experience – Understanding</h3>
  <div class="video-row">
    <div class="video-thumb" role="img" aria-label="Video still of a business meeting around a table"></div>
    <div class="video-thumb" role="img" aria-label="Video still of a consultant at work"></div>
    <div class="video-thumb" role="img" aria-label="Video still of a team in an office"></div>
  </div>
  <p>We guide you through our <strong>proven, strategic 4-Step Optimisation system</strong> to help your business reach its true potential. More than just consultants, Velor Quintess is a partner. Together we transform your business into the profitable venture it was meant to be.</p>
</section>

<section class="guide">
  <svg class="consult-arrow" width="700" height="360" viewBox="0 0 700 360">
    <path d="M0 180 L140 20 L140 70 L680 70 L680 300 L140 300 L140 340 Z" fill="#d3ebf8"/>
  </svg>
  <div class="guide-box">Our guide to the Velor Quintess <strong>4-Step Optimisation</strong> Process to see how and why it works.</div>
  <div class="btn-download">DOWNLOAD YOUR FREE COPY NOW!</div>
  <p class="consult-text"><strong>Your time is precious. Will you spend thirty minutes of it with us?</strong> We'd love to hear about <em>your plans and dreams</em>, and maybe we'll be a good fit.</p>
  <div class="consult-link">Online form to set up a Consultation</div>
</section>

<footer class="site-footer">
  <div class="foot-col contact">
    <h4>Get in touch with us today.</h4>
    <p>We will have a coffee with you, and show you a way to move towards a much more valuable future in terms of your business. This will be the best half hour you have spent.</p>
    <p class="phone">Call +61 2 5550 1234</p>
    <p class="mail">hello@velorquintess.net</p>
  </div>
  <div class="foot-col newsletter">
    <h4>Learn More!</h4>
    <p>Learn about the personal benefits to you the owner, read case studies, and understand the strategy and implementation process.</p>
    <h5>Sign up to our newsletter</h5>
    <div class="signup"><span class="field">Email Address</span><span class="go">GO</span></div>
  </div>
  <div class="foot-col sitemap">
    <h4>Sitemap</h4>
    <div class="sitemap-links">
      <ul><li>4-Step Solution</li><li>Why it Works</li><li>Who We Are</li><li>Case Studies</li><li>Privacy Policy</li></ul>
      <ul><li>About Us</li><li>FAQs</li><li>Blog</li><li>Contact Us</li></ul>
    </div>
  </div>
</footer>

<div class="bottom-bar">
  <span class="copyright">Copyright 2015 Velor Quintess | All Rights Reserved</span>
  <div class="socials"><span></span><span></span><span></span><span></span><span></span><span></span></div>
</div>

</body>
</html>
```